Business Card Design for Bright Harbor Paths, LLC

Using my logo created by Pixel Tide, please create a 2 sided business card that will have an lasting affect on my potential clients. I would like my name (Dennis R. Holt, MBA), title (Owner), phone numbers or Contact Info: 312 555-0148 and 312 555-0193. Website: http://www.brantleyfordcircle.com/dennisholt/. On the back side of the card use the Certified Brantley Ford Seal that I attached. You can decide to put either my company name or what I do or nothing at all.

Target Market(s)

Large to small business, owners, Information Technology Leaders, Government and City Leaders.

Industry/Entity Type

Business

Contact Information for Business Card

It is in the description. I would like my name (Dennis R. Holt, MBA), title (Owner), phone numbers or Contact Info: 312 555-0148 and 312 555-0193. Website: http://www.brantleyfordcircle.com/dennisholt/. On the back side of the card use the Certified Brantley Ford Seal that I attached.

Colors

Designer to choose colors to be used in the design.

Requirements
Must have
• Do not change the seal that is on the back or it's color.

```html
<!DOCTYPE html>
<html lang="en">
<head>
<meta charset="utf-8">
<title>Bright Harbor Paths, LLC — Business Card</title>
<link href="https://fonts.googleapis.com/css2?family=Cinzel:wght@500&family=Open+Sans:wght@300;400;700&display=swap" rel="stylesheet">
<style>
  :root {
    --canvas: #ececea;
    --card-dark: #1c1c1c;
    --card-light: #ffffff;
    --ink: #2a2a2a;
    --ink-soft: #5a5a5a;
    --silver: #c9c9c9;
    --seal-gold: #f2c418;
    --seal-gold-deep: #c99a0a;
    --accent-bar: #222222;
  }
  * { margin: 0; padding: 0; box-sizing: border-box; }
  html, body { width: 1200px; height: 800px; overflow: hidden; }
  body {
    background: var(--canvas);
    font-family: "Open Sans", Arial, sans-serif;
    position: relative;
  }
  .card {
    position: absolute;
    top: 246px;
    width: 540px;
    height: 308px;
    border-radius: 18px;
    box-shadow: 0 10px 30px rgba(0,0,0,0.18);
    overflow: hidden;
  }
  /* Back side */
  .card--back { left: 40px; background: var(--card-dark); }
  .back-wordmark {
    position: absolute;
    left: 0; right: 0; top: 138px;
    text-align: center;
    font-family: "Cinzel", Georgia, serif;
    font-weight: 500;
    font-size: 26px;
    letter-spacing: 1px;
    color: var(--silver);
  }
  .seal {
    position: absolute;
    right: 40px; top: 34px;
    width: 70px; height: 70px;
    border-radius: 50%;
    background: radial-gradient(circle at 40% 35%, #ffe36a, var(--seal-gold) 55%, var(--seal-gold-deep));
  }
  /* Front side */
  .card--front { left: 620px; background: var(--card-light); }
  .front-wordmark {
    position: absolute;
    right: 34px; top: 52px;
    font-family: "Cinzel", Georgia, serif;
    font-weight: 500;
    font-size: 19px;
    color: var(--ink);
  }
  .identity {
    position: absolute;
    left: 0; top: 122px;
    padding-left: 34px;
  }
  .identity::before {
    content: "";
    position: absolute;
    left: 0; top: 4px;
    width: 20px; height: 50px;
    background: linear-gradient(to bottom, #000, #777);
  }
  .person-name {
    font-size: 26px;
    font-weight: 300;
    color: var(--ink-soft);
    line-height: 1.1;
  }
  .person-name .surname { font-weight: 700; color: var(--ink); }
  .person-name .credential { font-size: 14px; font-weight: 400; color: var(--ink); }
  .person-title { font-size: 14px; color: var(--ink-soft); margin-top: 2px; }
  .contact-list {
    position: absolute;
    left: 34px; bottom: 30px;
    list-style: none;
    font-size: 13px;
    color: var(--ink);
  }
  .contact-list li { display: flex; align-items: center; gap: 10px; margin-top: 6px; }
  .contact-list svg { width: 13px; height: 13px; fill: var(--ink); flex: none; }
  .divider { margin: 0 10px; color: var(--ink-soft); }
</style>
</head>
<body>
  <section class="card card--back" aria-label="Business card back">
    <div class="seal" role="img" aria-label="Certified Brantley Ford seal"></div>
    <p class="back-wordmark">Bright Harbor Paths, LLC</p>
  </section>

  <section class="card card--front" aria-label="Business card front">
    <p class="front-wordmark">Bright Harbor Paths, LLC</p>
    <div class="identity">
      <p class="person-name">Dennis R. <span class="surname">Holt</span> <span class="credential">MBA</span></p>
      <p class="person-title">Owner</p>
    </div>
    <ul class="contact-list">
      <li>
        <svg viewBox="0 0 16 16" aria-hidden="true"><path d="M3 1h3l1.5 4-2 1.2a9 9 0 0 0 4.3 4.3l1.2-2 4 1.5v3a2 2 0 0 1-2 2A13 13 0 0 1 1 3a2 2 0 0 1 2-2z"/></svg>
        <span>312 555-0148<span class="divider">|</span>312 555-0193</span>
      </li>
      <li>
        <svg viewBox="0 0 16 16" aria-hidden="true"><path d="M1 3h14v10H1z M1 3l7 6 7-6" fill="none" stroke="#2a2a2a" stroke-width="1.6"/></svg>
        <span>dennis@brightharborpaths.com</span>
      </li>
      <li>
        <svg viewBox="0 0 16 16" aria-hidden="true"><path d="M8 0a5.5 5.5 0 0 0-5.5 5.5C2.5 10 8 16 8 16s5.5-6 5.5-10.5A5.5 5.5 0 0 0 8 0zm0 8a2.5 2.5 0 1 1 0-5 2.5 2.5 0 0 1 0 5z"/></svg>
        <span>www.brantleyfordcircle.com/dennisholt/</span>
      </li>
    </ul>
  </section>
</body>
</html>
```